Business Card Design

I need a business card and logo for a new company based in Manhattan, Kansas called "Ferncliff Works, LLC". I am a project management consultant. I specialize in laying the foundation for businesses and business owners to get their projects on track. Think of it as if you were wanting to go from coast to coast on a train. Before you can jump on the train and sell tickets, you have to design the path the train will take, acquire the land, clear the trees, level the ground, prepare the base for the track, lay the track and finally place the train on the track (That's what I do with my clients). Once the train is on the track and I've provided them with the operations manual, then they and their managers get to drive the train. I don't have color preferences. The final design should communicate a clear direction or path to growing the customer's business.
Updates

Since I am in need of a logo as well, I have also created a logo design project that will work in conjunction with this project.

Reason: Accepted a company logo this afternoon that I would like to have cards designed around. Sorry for jumping the gun and posting both projects at the same time.

Industry/Entity Type

Business

Contact Information for Business Card

Owner: Dale Purvis. Business Name: Ferncliff Works, LLC. Business Address: 4871 Marlow Bend, Manhattan, KS, 66921. Business Phone Number: 785-640-1572. Business Email: dale@ferncliffworksllc.example

```html
<!DOCTYPE html>
<html lang="en">
<head>
<meta charset="utf-8">
<title>Ferncliff Works, LLC — Business Card</title>
<link rel="stylesheet" href="https://fonts.googleapis.com/css2?family=Cinzel:wght@400&family=Open+Sans:wght@400;600;700&display=swap">
<style>
  :root {
    --backdrop: #e6e7ea;
    --card: #ffffff;
    --brand-blue: #1c6fb5;
    --ink-blue: #1f5aa8;
    --rule-blue: #1468b3;
    --faint-disc: #dde6f5;
    --faint-ring: #cdd4ea;
  }
  * { margin: 0; padding: 0; box-sizing: border-box; }
  html, body {
    width: 1200px; height: 864px; overflow: hidden;
    background: var(--backdrop);
  }
  .canvas {
    position: relative; width: 1200px; height: 864px;
    display: flex; align-items: center; justify-content: center;
  }
  .business-card {
    position: relative; width: 1040px; height: 594px;
    background: var(--card); overflow: hidden;
    box-shadow: 0 10px 30px rgba(0,0,0,0.12);
    font-family: "Open Sans", Arial, sans-serif;
    color: var(--ink-blue);
  }
  .backdrop-disc {
    position: absolute; left: 640px; top: -130px;
    width: 420px; height: 420px; border-radius: 50%;
    background: var(--faint-disc);
    border: 26px solid var(--faint-ring);
  }
  .brand-dot {
    position: absolute; left: 236px; top: 30px;
    width: 92px; height: 92px; border-radius: 50%;
    background: var(--brand-blue);
  }
  .company-name {
    position: absolute; left: 96px; top: 140px;
    font-family: "Cinzel", Georgia, serif; font-weight: 400;
    font-size: 44px; letter-spacing: 0.5px;
    color: var(--brand-blue); white-space: nowrap;
  }
  .divider {
    position: absolute; left: 226px; right: 0; top: 282px;
    height: 4px; background: var(--rule-blue);
  }
  .person {
    position: absolute; left: 110px; top: 238px;
  }
  .person-name {
    font-weight: 700; font-size: 32px; letter-spacing: 0.5px;
    text-transform: uppercase; line-height: 1.1;
  }
  .person-role {
    font-size: 22px; margin-left: 6px; line-height: 1.2;
  }
  .contact-list {
    position: absolute; left: 118px; top: 410px; list-style: none;
  }
  .contact-item {
    display: flex; align-items: center; gap: 16px;
    font-size: 23px; height: 46px;
  }
  .contact-icon { width: 26px; height: 22px; fill: var(--ink-blue); }
  .address {
    position: absolute; right: 60px; top: 412px;
    font-size: 23px; white-space: nowrap;
  }
</style>
</head>
<body>
<main class="canvas">
  <section class="business-card">
    <div class="backdrop-disc" aria-hidden="true"></div>
    <div class="brand-dot" aria-hidden="true"></div>
    <h1 class="company-name">Ferncliff Works, LLC</h1>

    <div class="divider" aria-hidden="true"></div>
    <div class="person">
      <p class="person-name">Dale Purvis</p>
      <p class="person-role">Owner</p>
    </div>

    <ul class="contact-list">
      <li class="contact-item">
        <svg class="contact-icon" viewBox="0 0 26 22" aria-hidden="true">
          <path d="M2 6c0-3 5-4 11-4s11 1 11 4v2h-5V6c-2-.6-4-.8-6-.8S9 5.4 7 6v2H2z"/>
          <path d="M6 9h14l3 11H3z"/>
        </svg>
        <span>785-640-1572</span>
      </li>
      <li class="contact-item">
        <svg class="contact-icon" viewBox="0 0 26 22" aria-hidden="true">
          <path d="M1 3h24v16H1z M3 5v1l10 7 10-7V5z" fill-rule="evenodd"/>
        </svg>
        <span>dale@ferncliffworksllc.example</span>
      </li>
    </ul>

    <p class="address">4871 Marlow Bend, Manhattan, KS, 66921</p>
  </section>
</main>
</body>
</html>
```